Business Advisory Cards in canvas model

I need a business card to start as an individual advising in business since I am "Bachelor in Business Creation and business innovation" I would like the "Canvas Model" (basic tool to land a business) to represent a part of the logo because it is the simplest and useful model to start, I will advise on business innovation and business creation. Detail: it can be formal, dynamic, colorful, that draws attention, adapted to the millenians.

Target Market(s)

People who want to create their own company. People seeking advice on: negotiation, innovation in business, desing thingking, business creation, coaching in organizational operations, business plan and canvas model.

Contact Information for Business Card

Puede ser colorida pero formal para negociar, que se vea moderna adaptada a los millenians, que se enfoque en “el modelo canvas”.
Que ocupe toda la tarjeta de ambos lados todo el diseño.

Font styles to use
Sans Serif

Colors

Designer to choose colors to be used in the design.

Requirements
Must have
• Canvas model
Nice to have
• Make it a card that makes the person who receives it want to contact the owner of the card. Make it pleasing to the eye.
Should not have
• Negative images, colors that are lost or damage the eyesight.

```html
<!DOCTYPE html>
<html lang="es">
<head>
<meta charset="utf-8">
<title>Bruno Salcedo – Tarjetas de presentación</title>
<link rel="stylesheet" href="https://fonts.googleapis.com/css2?family=Fira+Sans+Condensed:wght@500;600&family=Source+Sans+3:ital,wght@0,600;0,700;1,400;1,600;1,700&display=swap">
<style>
  :root {
    --navy: #0a1f8c;
    --navy-deep: #08207f;
    --navy-soft: #0f2d92;
    --sky: #7dd0e2;
    --sky-text: #7fd2e8;
    --ink: #0b2586;
    --white: #ffffff;
    --backdrop: #e8e6e3;
    --card-w: 700px;
    --card-h: 389px;
  }
  * { box-sizing: border-box; margin: 0; padding: 0; }
  html, body {
    width: 1200px; height: 855px; overflow: hidden;
    background: var(--backdrop);
  }
  .sheet { position: relative; width: 1200px; height: 855px; }

  .card {
    position: absolute; left: 250px;
    width: var(--card-w); height: var(--card-h);
    overflow: hidden;
    box-shadow: 0 4px 14px rgba(0,0,0,.18);
  }
  .card--back { top: 24px; background: var(--navy); }
  .card--front { top: 441px; background: var(--white); }

  /* Back: canvas-model grid */
  .cell { position: absolute; }
  .cell--navy { background: var(--navy); }
  .cell--deep { background: var(--navy-deep); }
  .cell--soft { background: var(--navy-soft); }
  .cell--sky { background: var(--sky); }

  .service {
    position: absolute;
    font-family: "Fira Sans Condensed", sans-serif;
    font-weight: 600; text-transform: uppercase;
    font-size: 17px; line-height: 1.22;
    color: var(--white);
  }
  .service--dark { color: var(--ink); }
  .service--wide {
    font-size: 21px; line-height: 1.42; color: var(--sky-text);
  }

  /* Front */
  .front-band {
    position: absolute; left: 0; top: 0;
    width: 100%; height: 268px; background: var(--navy);
  }
  .front-rule {
    position: absolute; top: 0; width: 1px; height: 268px;
    background: rgba(255,255,255,.12);
  }
  .owner-name {
    position: absolute; left: 6px; bottom: 121px;
    height: 268px;
    writing-mode: vertical-rl; transform: rotate(180deg);
    text-align: start;
    font-family: "Source Sans 3", sans-serif; font-weight: 700;
    font-size: 58px; line-height: 0.98; letter-spacing: .5px;
    color: var(--white); text-transform: uppercase;
  }
  .degree-lead {
    position: absolute; left: 280px; top: 19px;
    font-family: "Source Sans 3", sans-serif; font-style: italic; font-weight: 400;
    font-size: 22px; color: var(--white);
  }
  .degree-title {
    position: absolute; left: 431px; top: 19px;
    font-family: "Fira Sans Condensed", sans-serif; font-weight: 600;
    font-size: 22px; line-height: 1.4; color: var(--sky-text);
    text-transform: uppercase;
  }
  .contact-phone {
    position: absolute; left: 469px; top: 284px;
    font-family: "Source Sans 3", sans-serif; font-style: italic; font-weight: 400;
    font-size: 26px; color: var(--ink);
  }
  .tagline {
    position: absolute; left: 125px; top: 321px;
    font-family: "Fira Sans Condensed", sans-serif; font-weight: 600;
    font-size: 16px; color: var(--ink); text-transform: uppercase;
  }
  .tagline .accent { color: var(--sky-text); }
  .tagline-bar {
    position: absolute; left: 355px; top: 325px;
    width: 59px; height: 14px; background: var(--ink);
  }
  .contact-email {
    position: absolute; left: 420px; top: 316px;
    font-family: "Source Sans 3", sans-serif; font-style: italic; font-weight: 700;
    font-size: 21px; color: var(--ink);
  }
</style>
</head>
<body>
<main class="sheet">

  <section class="card card--back" aria-label="Reverso: servicios en modelo canvas">
    <div class="cell cell--navy" style="left:0;top:0;width:140px;height:122px"></div>
    <div class="cell cell--sky" style="left:0;top:122px;width:140px;height:122px"></div>
    <div class="cell cell--navy" style="left:140px;top:0;width:140px;height:244px"></div>
    <div class="cell cell--deep" style="left:280px;top:0;width:140px;height:244px"></div>
    <div class="cell cell--deep" style="left:420px;top:0;width:140px;height:122px"></div>
    <div class="cell cell--soft" style="left:420px;top:122px;width:140px;height:122px"></div>
    <div class="cell cell--sky" style="left:560px;top:0;width:140px;height:122px"></div>
    <div class="cell cell--navy" style="left:560px;top:122px;width:140px;height:122px"></div>
    <div class="cell cell--soft" style="left:0;top:244px;width:349px;height:145px"></div>
    <div class="cell cell--sky" style="left:349px;top:244px;width:351px;height:145px"></div>

    <p class="service" style="left:142px;top:50px">Asesorías en<br>desarrollo<br>organizacional</p>
    <p class="service" style="left:282px;top:172px">Asesorías<br>en creación<br>de negocios</p>
    <p class="service" style="left:422px;top:200px">Coaching<br>en ventas</p>
    <p class="service service--dark" style="left:560px;top:102px">Conferencias</p>
    <p class="service service--wide" style="left:20px;top:297px">Coaching en estrategias<br>y administración de operaciones</p>
  </section>

  <section class="card card--front" aria-label="Anverso: datos de contacto">
    <div class="front-band"></div>
    <div class="front-rule" style="left:140px"></div>
    <div class="front-rule" style="left:558px"></div>

    <h1 class="owner-name">Bruno<br>Salcedo</h1>
    <p class="degree-lead">Licenciado en</p>
    <p class="degree-title">Creación de negocios<br>e innovación<br>empresarial</p>

    <p class="contact-phone">55 4810 2297</p>
    <p class="tagline">Ideate <span class="accent">prototype</span> &amp; <span class="accent">launch</span></p>
    <div class="tagline-bar"></div>
    <p class="contact-email">hola@brunosalcedo.mx</p>
  </section>

</main>
</body>
</html>
```